need eczema bath soak label/bag

need you to recreate this please. ai file. recreate this exact image please. ...if you want a big tip, create some different styles.

Colors
0054AA
0677BA
7BADD7
CADEEF
E8F1F8

```html
<!DOCTYPE html>
<html lang="en">
<head>
<meta charset="utf-8">
<title>The Ocean Healed My Bag</title>
<link rel="stylesheet" href="https://fonts.googleapis.com/css2?family=Montserrat:wght@600;700;800&display=swap">
<style>
  :root {
    --ink: #0f2a48;
    --surf-foam: #e9f6f4;
    --surf-teal: #3dbcb8;
    --surf-deep: #2aa6ab;
    --shore-foam: #f3f7f4;
    --sand-warm: #f5bfa3;
    --sand-light: #fbe3d7;
  }
  html, body {
    margin: 0;
    padding: 0;
    overflow: hidden;
    background: #ffffff;
  }
  .label {
    position: relative;
    width: 801px;
    height: 1200px;
    overflow: hidden;
    font-family: "Montserrat", Arial, sans-serif;
    color: var(--ink);
    text-align: center;
  }
  .label__scene {
    position: absolute;
    inset: 0;
    background: linear-gradient(175deg,
      var(--surf-foam) 0%,
      #bfe6e2 10%,
      var(--surf-teal) 22%,
      var(--surf-deep) 38%,
      #56c9c1 50%,
      var(--shore-foam) 58%,
      #f8d6c4 64%,
      var(--sand-warm) 72%,
      #f8cdb7 85%,
      var(--sand-light) 100%);
  }
  .label__content {
    position: absolute;
    inset: 0;
  }
  .headline {
    position: absolute;
    top: 300px;
    left: 0;
    right: 0;
    margin: 0;
    font-weight: 800;
    letter-spacing: 4px;
    line-height: 1;
  }
  .headline__lead {
    display: block;
    font-size: 38px;
    letter-spacing: 6px;
    margin-bottom: 22px;
  }
  .headline__line {
    display: block;
    font-size: 70px;
    margin-bottom: 18px;
  }
  .blurb {
    position: absolute;
    top: 662px;
    left: 0;
    right: 0;
    margin: 0;
    font-size: 11px;
    font-weight: 700;
    letter-spacing: 0.6px;
    line-height: 25px;
  }
  .product-name {
    position: absolute;
    top: 760px;
    left: 0;
    right: 0;
    margin: 0;
    font-size: 18px;
    font-weight: 700;
    letter-spacing: 1px;
  }
  .batch-code {
    position: absolute;
    top: 806px;
    left: 0;
    right: 0;
    margin: 0;
    font-size: 23px;
    font-weight: 800;
    transform: rotate(4deg);
  }
  .brand {
    position: absolute;
    top: 944px;
    left: 0;
    right: 0;
    display: flex;
    flex-direction: column;
    align-items: center;
  }
  .brand__square {
    width: 86px;
    height: 86px;
    background: var(--ink);
  }
  .brand__name {
    margin-top: 36px;
    font-size: 24px;
    font-weight: 800;
    letter-spacing: 4px;
  }
</style>
</head>
<body>
  <main class="label">
    <div class="label__scene" role="img" aria-label="Aerial photograph of turquoise ocean waves breaking onto a pale peach sandy beach"></div>
    <div class="label__content">
      <h1 class="headline">
        <span class="headline__lead">THE</span>
        <span class="headline__line">OCEAN</span>
        <span class="headline__line">HEALED</span>
        <span class="headline__line">MY A BAG</span>
      </h1>
      <p class="blurb">
        A GENTLE SEA SALT SOAK FOR DRY SKIN<br>
        CALMS ITCHY PATCHES AND SOFTENS ROUGH AREAS<br>
        MADE WITH OATMEAL AND MINERAL RICH SALTS
      </p>
      <p class="product-name">OCEAN I &nbsp;IN A BA</p>
      <p class="batch-code">B 77 6. : 119</p>
      <div class="brand">
        <div class="brand__square"></div>
        <div class="brand__name">TIDEWELL</div>
      </div>
    </div>
  </main>
</body>
</html>
```